brisk-vale.com Real Estate, Investment, Financial corporate

Real Estate, Investment, Financial corporate looking site. Show present a professional firm, with an elegant display. Please see the attached file which includes the logo, palette and fonts.
Updates

We just starting the brief today. ( logo was delayed)

Target Market(s)

Investors, Corporate , B2b

Industry/Entity Type

real-estate investments

Number of Pages Required

3 page

Requirements
Must have
• Dazzling Homepage
Nice to have
• paralex

```html
<!DOCTYPE html>
<html lang="en">
<head>
<meta charset="utf-8">
<title>Brisk Vale — Real Estate, Investment, Financial Corporate</title>
<link href="https://fonts.googleapis.com/css2?family=Libre+Baskerville:wght@400;700&family=Open+Sans:ital,wght@0,400;0,600;0,700;1,400&display=swap" rel="stylesheet">
<style>
:root{
  --blue:#2a63b5;
  --blue-dark:#1f4f95;
  --ink:#2b2b2b;
  --text:#555;
  --muted:#777;
  --grey-bg:#f2f2f2;
  --dark-btn:#333;
  --footer:#131313;
  --white:#fff;
  --serif:"Libre Baskerville", Georgia, serif;
  --sans:"Open Sans", Arial, sans-serif;
}
*{box-sizing:border-box;margin:0;padding:0}
html,body{width:1200px;height:4200px;overflow:hidden}
body{position:relative;background:var(--white);font-family:var(--sans);color:var(--text)}
.abs{position:absolute}

/* header */
.logo{left:173px;top:24px;font-family:var(--serif);font-weight:700;font-size:28px;line-height:1.05;color:var(--blue);letter-spacing:1px;z-index:3}
.nav{right:173px;top:36px;display:flex;gap:28px;z-index:3}
.nav a{font-size:15px;font-weight:600;color:#222;text-decoration:none;letter-spacing:.3px}

/* hero */
.hero-photo{left:0;top:0;width:1200px;height:780px;
  background:linear-gradient(160deg,#eef0f0 0%,#d9dcdb 30%,#c8b79c 55%,#6f7e96 75%,#9fb0c7 100%)}
.hero-title{left:147px;top:326px;width:432px;height:103px;background:rgba(42,99,181,.88);
  font-family:var(--serif);font-weight:700;font-size:56px;color:var(--white);display:flex;align-items:center;justify-content:center;letter-spacing:1px}

/* service band */
.band{left:0;top:660px;width:1200px;height:560px}
.service{width:300px;text-align:center}
.service svg{display:block;margin:0 auto}
.service h3{font-family:var(--serif);font-weight:400;font-size:21px;color:var(--ink);margin-top:18px;letter-spacing:.5px}
.service h3.accent{color:var(--blue)}
.service p{font-size:13.5px;line-height:23px;color:var(--text);margin-top:12px}
.btn{display:inline-block;font-size:12.5px;font-weight:600;color:var(--white);background:var(--dark-btn);padding:12px 10px;border-radius:3px;text-decoration:none}
.btn-blue{background:var(--blue)}
.service .btn{margin-top:22px}

/* about */
.about-title{left:173px;top:1287px;font-family:var(--serif);font-weight:700;font-size:32px;color:var(--ink)}
.about-title span{color:var(--blue)}
.about-copy{left:173px;top:1340px;width:448px;font-size:12.5px;line-height:24px;text-align:justify}
.about-copy p+p{margin-top:12px}
.about-btn{left:173px;top:1589px;padding:14px 10px}
.about-photo{left:664px;top:1243px}

/* listings */
.listings-bg{left:0;top:1745px;width:1200px;height:472px}
.section-title{width:1200px;left:0;text-align:center;font-family:var(--serif);font-weight:700;font-size:31px;letter-spacing:.5px}
.listings-title{top:1897px;color:var(--white)}
.listing{top:1997px;width:274px;height:464px;background:var(--white);box-shadow:0 4px 14px rgba(0,0,0,.12)}
.listing-photo{height:220px}
.listing-body{padding:18px 12px 0}
.price{font-family:var(--serif);font-weight:700;font-size:19px;color:var(--blue)}
.listing h4{font-family:var(--serif);font-weight:400;font-size:17px;color:var(--ink);margin-top:14px;letter-spacing:.4px}
.listing p{font-size:12.5px;line-height:22.5px;margin-top:10px;text-align:justify}
.agent{position:absolute;left:0;bottom:0;width:100%;height:68px;border-top:1px solid #ddd;display:flex;align-items:center;padding:0 14px}
.avatar{width:46px;height:46px;border-radius:50%;background:linear-gradient(135deg,#c9ccd2,#8a93a3)}
.agent-name{margin-left:14px;font-size:12px;color:var(--ink);line-height:17px}
.agent-name em{display:block;font-size:10.5px;color:var(--muted)}
.agent-icons{margin-left:auto;display:flex;gap:10px}

/* feedback */
.feedback-bg{left:0;top:2520px;width:1200px;height:694px}
.feedback-title{top:2677px;color:var(--ink)}
.feedback-title span{color:var(--blue)}
.quote-card{background:var(--white);box-shadow:0 4px 14px rgba(0,0,0,.08);overflow:hidden}
.quote-badge{position:absolute;border-radius:50%;display:flex;align-items:center;justify-content:center;color:var(--white);font-family:var(--serif);font-weight:700}
.quote-ghost{position:absolute;font-family:var(--serif);font-weight:700;color:#eef2f8;line-height:1}
.quote-card h5{position:absolute;font-weight:400;color:var(--ink)}
.quote-card p{position:absolute;line-height:2.45;text-align:justify;color:#444}
.quote-card .by{position:absolute;color:var(--ink);line-height:1}

/* photo strip */
.strip{top:3214px;width:400px;height:457px}
.strip-caption{position:absolute;left:24px;top:378px;display:flex;gap:16px;align-items:flex-start;color:var(--white);font-size:20px;line-height:29px;font-weight:600}
.strip-caption svg{margin-top:10px;flex:none}

/* footer */
.footer{left:0;top:3671px;width:1200px;height:529px;background:var(--footer)}
.footer-col{top:3776px;color:var(--white)}
.footer-col h6{font-size:19px;font-weight:600;letter-spacing:.3px}
.footer-col ul{list-style:none;margin-top:12px}
.footer-col li{font-size:13px;line-height:28.5px;color:#e8e8e8}
.footer-col p{font-size:13px;line-height:28.5px;color:#e8e8e8;margin-top:12px;width:240px}
.email{left:804px;top:3889px;width:223px;height:52px;background:var(--white);border-radius:2px;font-size:13px;color:#333;padding:17px 12px}
.subscribe{left:804px;top:3958px;width:103px;height:52px;background:var(--blue);color:var(--white);font-size:13px;font-weight:600;display:flex;align-items:center;justify-content:center;border-radius:2px}
.footer-rule{left:173px;top:4083px;width:854px;height:1px;background:#555}
.copyright{left:0;top:4129px;width:1200px;text-align:center;color:var(--white);font-size:13px;font-weight:600}
</style>
</head>
<body>

<!-- hero -->
<div class="abs hero-photo" role="img" aria-label="Photo of a smiling couple being shown a bright modern home by an estate agent"></div>
<div class="abs logo">BRISK<br>VALE</div>
<nav class="abs nav">
  <a>HOME</a><a>ABOUT US</a><a>REAL ESTATE</a><a>BLOG</a><a>CONTACT</a>
</nav>
<div class="abs hero-title">BRISK VALE</div>

<!-- services band -->
<svg class="abs band" width="1200" height="560" viewBox="0 0 1200 560">
  <path d="M0 16 Q600 196 1200 16 L1200 546 Q600 400 0 546 Z" fill="var(--blue)"/>
  <path d="M46 70 Q220 100 386 139 L386 435 Q220 460 46 489 Z" fill="#fff"/>
  <path d="M429 139 Q599 135 769 139 L769 435 Q599 432 429 435 Z" fill="#fff"/>
  <path d="M813 139 Q980 100 1154 70 L1154 489 Q980 460 813 435 Z" fill="#fff"/>
</svg>

<div class="abs service" style="left:66px;top:815px">
  <svg width="64" height="62" viewBox="0 0 64 62" fill="none" stroke="#222" stroke-width="2.4" stroke-linejoin="round">
    <path d="M8 26 L32 6 L56 26"/><path d="M14 21 V52 H50 V21"/><path d="M26 52 V36 H38 V52"/><path d="M4 46 H22 L30 40"/>
  </svg>
  <h3>REAL ESTATE</h3>
  <p>Nemo enim ipsam voluptatem quia voluptas sit aspernatur aut odit aut fugit, sed quia consequuntur magnis</p>
  <a class="btn">READ MORE</a>
</div>
<div class="abs service" style="left:449px;top:815px">
  <svg width="64" height="62" viewBox="0 0 64 62">
    <path d="M24 20 L40 20 L36 12 L28 12 Z" fill="var(--blue)"/>
    <path d="M22 22 Q10 34 16 48 Q32 56 48 48 Q54 34 42 22 Z" fill="var(--blue)"/>
    <text x="32" y="44" text-anchor="middle" font-family="Open Sans, sans-serif" font-weight="700" font-size="18" fill="#fff">$</text>
    <path d="M50 6 V16 M45 11 H55" stroke="var(--blue)" stroke-width="3"/>
    <path d="M2 44 H12 L20 52 H36" stroke="var(--blue)" stroke-width="3" fill="none"/>
  </svg>
  <h3 class="accent">INVESTMENT</h3>
  <p>Nemo enim ipsam voluptatem quia voluptas sit aspernatur aut odit aut fugit, sed quia consequuntur magnis</p>
  <a class="btn btn-blue">READ MORE</a>
</div>
<div class="abs service" style="left:833px;top:815px">
  <svg width="64" height="62" viewBox="0 0 64 62" fill="none" stroke="#222" stroke-width="2.2">
    <circle cx="28" cy="30" r="22"/><ellipse cx="28" cy="30" rx="10" ry="22"/><path d="M6 30 H50 M10 19 H46 M10 41 H40"/>
    <text x="52" y="48" text-anchor="middle" font-family="Open Sans, sans-serif" font-size="24" fill="#222" stroke="none">$</text>
  </svg>
  <h3>FINANCIAL CORPORATE</h3>
  <p>Nemo enim ipsam voluptatem quia voluptas sit aspernatur aut odit aut fugit, sed quia consequuntur magnis</p>
  <a class="btn">READ MORE</a>
</div>

<!-- about -->
<h2 class="abs about-title">ABOUT <span>BRISK-VALE</span></h2>
<div class="abs about-copy">
  <p>Nam libero tempore, cum soluta nobis est eligendi optio cumque nihil impedit quo minus id quod maxime placeat facere possimus, omnis voluptas assumenda est, omnis dolor repellendus. Temporibus autem quibusdam et aut officiis debitis aut rerum necessitatibus saepe eveniet ut et voluptates repudiandae sint et molestiae non recusandae. Itaque earum rerum hic tenetur a sapiente delectus.</p>
  <p>Temporibus autem quibusdam et aut officiis debitis aut rerum necessitatibus saepe eveniet ut et voluptates repudiandae sint et molestiae non recusandae. Itaque earum rerum hic tenetur a sapiente delectus.</p>
</div>
<a class="abs btn btn-blue about-btn">READ MORE</a>
<svg class="abs about-photo" width="480" height="450" viewBox="0 0 480 450" role="img" aria-label="Photo of a businessman reviewing documents at a laptop beside a brick wall">
  <defs>
    <linearGradient id="aboutTone" x1="0" y1="0" x2="1" y2="1">
      <stop offset="0" stop-color="#9a6a58"/><stop offset=".45" stop-color="#4f5665"/><stop offset="1" stop-color="#c9ccd3"/>
    </linearGradient>
  </defs>
  <path d="M260 6 C330 8 340 70 400 90 C460 110 478 190 468 260 C458 340 420 420 320 440 C230 458 170 420 110 400 C40 378 2 330 4 260 C6 180 60 150 110 110 C160 70 190 4 260 6 Z" fill="var(--blue)"/>
  <path d="M262 16 C322 18 330 78 388 100 C446 122 462 196 452 262 C442 336 406 410 316 428 C232 444 178 408 116 390 C52 370 14 326 16 262 C18 190 70 160 118 122 C164 86 196 14 262 16 Z" fill="url(#aboutTone)" transform="translate(6 -4)"/>
</svg>

<!-- featured listings -->
<svg class="abs listings-bg" width="1200" height="472" viewBox="0 0 1200 472">
  <path d="M0 4 Q600 150 1200 4 L1200 472 L0 472 Z" fill="var(--blue)"/>
</svg>
<h2 class="abs section-title listings-title">FEATURED LISTINGS</h2>

<article class="abs listing" style="left:173px">
  <div class="listing-photo" role="img" aria-label="Photo of a white two-storey family house with garden" style="background:linear-gradient(180deg,#cfe1f2 0%,#e9ecef 45%,#6c8a4f 100%)"></div>
  <div class="listing-body">
    <div class="price">$ 200.00</div>
    <h4>MODERN APARTMENTS</h4>
    <p>Nemo enim ipsam voluptatem quia voluptas sit aspernatur aut odit aut fugit, sed quia consequuntur magnis</p>
  </div>
  <div class="agent">
    <div class="avatar" role="img" aria-label="Agent portrait"></div>
    <div class="agent-name">Mark Delaney<em>Estate Agent</em></div>
    <div class="agent-icons">
      <svg width="20" height="20" viewBox="0 0 20 20" fill="none" stroke="#333" stroke-width="1.5"><path d="M10 17 L3 10 A4 4 0 0 1 10 5 A4 4 0 0 1 17 10 Z"/></svg>
      <svg width="20" height="20" viewBox="0 0 20 20" fill="none" stroke="#333" stroke-width="1.5"><circle cx="10" cy="10" r="8"/><path d="M10 6 V14 M6 10 H14"/></svg>
    </div>
  </div>
</article>
<article class="abs listing" style="left:463px">
  <div class="listing-photo" role="img" aria-label="Photo of a wooden staircase in a bright luxury interior" style="background:linear-gradient(135deg,#f1eee8 0%,#c9b59a 45%,#7a4a2c 100%)"></div>
  <div class="listing-body">
    <div class="price">$ 200.00</div>
    <h4>LUXURY APARTMENTS</h4>
    <p>Nemo enim ipsam voluptatem quia voluptas sit aspernatur aut odit aut fugit, sed quia consequuntur magnis</p>
  </div>
  <div class="agent">
    <div class="avatar" role="img" aria-label="Agent portrait"></div>
    <div class="agent-name">Mark Delaney<em>Estate Agent</em></div>
    <div class="agent-icons">
      <svg width="20" height="20" viewBox="0 0 20 20" fill="none" stroke="#333" stroke-width="1.5"><path d="M10 17 L3 10 A4 4 0 0 1 10 5 A4 4 0 0 1 17 10 Z"/></svg>
      <svg width="20" height="20" viewBox="0 0 20 20" fill="none" stroke="#333" stroke-width="1.5"><circle cx="10" cy="10" r="8"/><path d="M10 6 V14 M6 10 H14"/></svg>
    </div>
  </div>
</article>
<article class="abs listing" style="left:753px">
  <div class="listing-photo" role="img" aria-label="Photo of a modern bedroom with a made bed and wooden floor" style="background:linear-gradient(160deg,#3d4550 0%,#8c8f94 40%,#e9e4dc 70%,#7b4b2a 100%)"></div>
  <div class="listing-body">
    <div class="price">$ 200.00</div>
    <h4>COMFORT APARTMENTS</h4>
    <p>Nemo enim ipsam voluptatem quia voluptas sit aspernatur aut odit aut fugit, sed quia consequuntur magnis</p>
  </div>
  <div class="agent">
    <div class="avatar" role="img" aria-label="Agent portrait"></div>
    <div class="agent-name">Mark Delaney<em>Estate Agent</em></div>
    <div class="agent-icons">
      <svg width="20" height="20" viewBox="0 0 20 20" fill="none" stroke="#333" stroke-width="1.5"><path d="M10 17 L3 10 A4 4 0 0 1 10 5 A4 4 0 0 1 17 10 Z"/></svg>
      <svg width="20" height="20" viewBox="0 0 20 20" fill="none" stroke="#333" stroke-width="1.5"><circle cx="10" cy="10" r="8"/><path d="M10 6 V14 M6 10 H14"/></svg>
    </div>
  </div>
</article>

<!-- clients feedback -->
<svg class="abs feedback-bg" width="1200" height="694" viewBox="0 0 1200 694">
  <path d="M0 0 Q600 160 1200 0 L1200 694 L0 694 Z" fill="var(--grey-bg)"/>
</svg>
<h2 class="abs section-title feedback-title">CLIENTS <span>FEEDBACK</span></h2>

<div class="abs quote-card" style="left:-20px;top:2799px;width:354px;height:278px">
  <div class="quote-ghost" style="left:-10px;top:90px;font-size:190px">“</div>
  <div class="quote-badge" style="left:-44px;top:-4px;width:90px;height:90px;background:#2b2b2b;font-size:60px;padding-top:30px">“</div>
  <h5 style="left:82px;top:26px;font-size:17px">Great Work</h5>
  <p style="left:82px;top:62px;width:244px;font-size:10.5px">“Nam libero tempore, cum soluta nobis est eligendi optio cumque nihil impedit quo minus id quod maxime placeat facere possimus, omnis voluptas assumenda est, omnis dolor repellendus. Temporibus autem quibusdam et aut officiis debitis aut rerum...”</p>
  <div class="by" style="left:82px;top:238px;font-size:12px">- Thomas</div>
</div>

<div class="abs quote-card" style="left:375px;top:2776px;width:450px;height:329px;overflow:visible">
  <div class="quote-ghost" style="left:8px;top:110px;font-size:230px">“</div>
  <div class="quote-badge" style="left:0;top:0;width:106px;height:106px;border-radius:0 50% 50% 50%;background:var(--blue);font-size:72px;padding-top:36px">“</div>
  <h5 style="left:132px;top:38px;font-size:19px">Great Work</h5>
  <p style="left:132px;top:80px;width:284px;font-size:12px">“Nam libero tempore, cum soluta nobis est eligendi optio cumque nihil impedit quo minus id quod maxime placeat facere possimus, omnis voluptas assumenda est, omnis dolor repellendus. Temporibus autem quibusdam et aut officiis debitis aut rerum...”</p>
  <div class="by" style="left:132px;top:282px;font-size:14px">- Alexander</div>
</div>

<div class="abs quote-card" style="left:864px;top:2799px;width:354px;height:278px">
  <div class="quote-ghost" style="left:10px;top:90px;font-size:190px">“</div>
  <div class="quote-badge" style="left:0;top:0;width:90px;height:90px;border-radius:0 50% 50% 50%;background:#2b2b2b;font-size:60px;padding-top:30px">“</div>
  <h5 style="left:113px;top:26px;font-size:17px">Great Work</h5>
  <p style="left:113px;top:62px;width:244px;font-size:10.5px">“Nam libero tempore, cum soluta nobis est eligendi optio cumque nihil impedit quo minus id quod maxime placeat facere possimus, omnis voluptas assumenda est, omnis dolor repellendus. Temporibus autem quibusdam et aut officiis debitis aut rerum...”</p>
  <div class="by" style="left:113px;top:238px;font-size:12px">- Thomas</div>
</div>

<!-- photo strip -->
<div class="abs strip" style="left:0" role="img" aria-label="Photo of an architect pointing at a scale model of an apartment tower">
  <div style="position:absolute;inset:0;background:linear-gradient(180deg,#d7dde3 0%,#8e9aa8 50%,#2a2f36 85%,#1a1c1f 100%)"></div>
  <div class="strip-caption"><svg width="22" height="24" viewBox="0 0 22 24"><path d="M0 0 L22 12 L0 24 Z" fill="#fff"/></svg><span>Nam libero tempore, cum soluta<br>nobis optio cumque nihil</span></div>
</div>
<div class="abs strip" style="left:400px" role="img" aria-label="Photo of a young couple reviewing documents with an advisor at home">
  <div style="position:absolute;inset:0;background:linear-gradient(180deg,#ebe6dc 0%,#a89478 45%,#3a3430 85%,#1c1a18 100%)"></div>
  <div class="strip-caption"><svg width="22" height="24" viewBox="0 0 22 24"><path d="M0 0 L22 12 L0 24 Z" fill="#fff"/></svg><span>Nam libero tempore, cum soluta<br>nobis optio cumque nihil</span></div>
</div>
<div class="abs strip" style="left:800px" role="img" aria-label="Photo of a smiling businesswoman in a bright office with colleagues behind">
  <div style="position:absolute;inset:0;background:linear-gradient(180deg,#eeeae4 0%,#b7a99a 45%,#3e3833 85%,#1c1a18 100%)"></div>
  <div class="strip-caption"><svg width="22" height="24" viewBox="0 0 22 24"><path d="M0 0 L22 12 L0 24 Z" fill="#fff"/></svg><span>Nam libero tempore, cum soluta<br>nobis optio cumque nihil</span></div>
</div>

<!-- footer -->
<footer class="abs footer"></footer>
<div class="abs footer-col" style="left:173px">
  <h6>COMPANY</h6>
  <ul><li>About</li><li>Blog</li><li>All Products</li><li>Locations Map</li><li>FAQ</li><li>Contact us</li></ul>
</div>
<div class="abs footer-col" style="left:367px">
  <h6>SERVICES</h6>
  <ul><li>Order tracking</li><li>Wish List</li><li>Login</li><li>My account</li><li>Terms &amp; Conditions</li><li>Promotional Offers</li></ul>
</div>
<div class="abs footer-col" style="left:584px">
  <h6>CUSTOMER CARE</h6>
  <ul><li>Login</li><li>My account</li><li>Wish List</li><li>Order tracking</li><li>FAQ</li><li>Contact us</li></ul>
</div>
<div class="abs footer-col" style="left:804px">
  <h6>NEWSLETTER</h6>
  <p>Subscribe to our weekly Newsletter and receive updates via email.</p>
</div>
<div class="abs email">Email</div>
<div class="abs subscribe">SUBSCRIBE</div>
<div class="abs footer-rule"></div>
<div class="abs copyright">COPYRIGHTS @ 2021 BRISK-VALE.</div>

</body>
</html>
```